Presentation folder

We are an education provider located in Sydney, Australia. We offer training courses in Business, Hospitality, Tourism and also English language courses. Our students are young adults - average age 24 - from many different countries.
We are after a A4 size presentation folder to hold all our course flyers, price lists, special offers etc. The folder will have one pocket on inside right with slits for business card. We want full colour printing throughout.
The finished product will be displayed on brochure stands (along with loads of competitor brochures) in our representative offices around the world.
We need the four-page full-colour design to be print ready.
Attached you will find:
* Required text
* Some of our design ideas (for front cover only)
* The photos used in our designs
* Some competitor samples
* Our logos
* Our old brochure showing our location map on the last page
* Some of our current flyers in use
* Folder template - not sure if its useable though

```html
<!DOCTYPE html>
<html lang="en">
<head>
<meta charset="utf-8">
<title>Kestrel College Presentation Folder – Inside Spread</title>
<link rel="stylesheet" href="https://fonts.googleapis.com/css2?family=Parisienne&family=Questrial&display=swap">
<style>
  :root {
    --paper: #e8f4f9;
    --tile-light: #bcdcf0;
    --tile-mid: #8fbde6;
    --tile-deep: #6f8fc8;
    --heading-red: #8c1c2c;
    --body-ink: #4d5a86;
    --fold-line: #c9dbe4;
    --photo-warm: #b58a6a;
    --photo-cool: #7fa2c4;
  }
  * { margin: 0; padding: 0; box-sizing: border-box; }
  html, body {
    width: 1200px; height: 863px; overflow: hidden; background: #ffffff;
  }
  .folder-spread {
    position: relative; width: 1200px; height: 863px;
    background: var(--paper); overflow: hidden;
  }
  .tile-wave { position: absolute; inset: 0; }
  .spread-structure { position: absolute; inset: 0; }

  .welcome {
    position: absolute; left: 118px; top: 56px; width: 425px;
  }
  .welcome-title {
    font-family: "Parisienne", cursive;
    font-weight: 400; font-size: 24px; line-height: 28px;
    color: var(--heading-red);
    margin-bottom: 8px;
  }
  .welcome p {
    font-family: "Questrial", sans-serif;
    font-size: 11.8px; line-height: 12.4px; color: var(--body-ink);
    text-align: justify; margin-bottom: 16px;
  }

  .photo {
    position: absolute;
    box-shadow: 4px 6px 10px rgba(40, 60, 90, 0.55);
    border: 1px solid #ffffff;
  }
  .photo-study {
    left: 80px; top: 378px; width: 177px; height: 118px;
    background: linear-gradient(135deg, #6b5a4e 0%, var(--photo-warm) 45%, #d9d2c4 100%);
  }
  .photo-group {
    left: 219px; top: 530px; width: 187px; height: 124px;
    background: linear-gradient(160deg, #c9a98a 0%, #a33a2e 50%, #7a5a48 100%);
  }
  .photo-traveller {
    left: 345px; top: 690px; width: 195px; height: 130px;
    background: linear-gradient(120deg, var(--photo-cool) 0%, #d8c9a0 55%, #eae4d6 100%);
  }

  .brand-row {
    position: absolute; left: 37px; top: 776px;
    display: flex; flex-direction: column; gap: 10px;
  }
  .brand {
    display: flex; align-items: center; gap: 7px;
    font-family: "Questrial", sans-serif; font-weight: 400;
    font-size: 14px; line-height: 16px; color: var(--body-ink);
  }
  .brand-mark { width: 9px; height: 9px; background: var(--body-ink); }
</style>
</head>
<body>
<main class="folder-spread">

  <svg class="tile-wave" viewBox="0 0 1200 863" role="img" aria-label="Decorative sweeping wave of small light-to-mid blue mosaic tiles">
    <defs>
      <linearGradient id="waveLeft" x1="0" y1="0" x2="1" y2="1">
        <stop offset="0" stop-color="#bcdcf0" stop-opacity="0.5"/>
        <stop offset="0.55" stop-color="#8fbde6" stop-opacity="0.75"/>
        <stop offset="1" stop-color="#bcdcf0" stop-opacity="0.6"/>
      </linearGradient>
      <linearGradient id="waveRight" x1="0" y1="0" x2="1" y2="1">
        <stop offset="0" stop-color="#bcdcf0" stop-opacity="0.45"/>
        <stop offset="0.5" stop-color="#6f8fc8" stop-opacity="0.7"/>
        <stop offset="1" stop-color="#8fbde6" stop-opacity="0.75"/>
      </linearGradient>
    </defs>
    <path d="M0 60 C 40 250, 200 380, 360 560 C 450 660, 520 760, 560 863 L 380 863 C 330 760, 230 640, 120 540 C 40 470, 0 400, 0 330 Z" fill="url(#waveLeft)"/>
    <path d="M0 380 C 60 480, 150 560, 260 650 C 330 710, 380 790, 400 863 L 300 863 C 260 790, 180 710, 90 650 C 40 620, 0 580, 0 540 Z" fill="url(#waveLeft)" opacity="0.6"/>
    <path d="M600 40 C 620 240, 760 360, 900 450 C 1020 530, 1100 600, 1200 700 L 1200 863 L 1090 863 C 1040 740, 960 640, 860 570 C 720 470, 610 380, 600 260 Z" fill="url(#waveRight)"/>
    <path d="M620 0 L 680 0 C 700 120, 780 220, 900 300 C 1000 370, 1120 430, 1200 520 L 1200 600 C 1110 500, 1000 430, 880 360 C 760 290, 640 180, 620 0 Z" fill="url(#waveRight)" opacity="0.45"/>
  </svg>

  <svg class="spread-structure" viewBox="0 0 1200 863" aria-hidden="true">
    <defs>
      <filter id="pocketShadow" x="-10%" y="-10%" width="130%" height="130%">
        <feDropShadow dx="-3" dy="-3" stdDeviation="5" flood-color="#5a6f80" flood-opacity="0.35"/>
      </filter>
    </defs>
    <line x1="600" y1="0" x2="600" y2="863" stroke="#c9dbe4" stroke-width="1"/>
    <path d="M1078 16 L 1192 4 L 1200 4 L 1200 863 L 1078 863 Z" fill="#e8f4f9" fill-opacity="0.35" stroke="#b7c9d3" stroke-width="1.2"/>
    <path d="M700 634 L 1080 640 L 1200 640 L 1200 863 L 608 863 Z" fill="#e8f4f9" fill-opacity="0.55" filter="url(#pocketShadow)" stroke="#c2d2da" stroke-width="1"/>
    <g stroke="#6a7580" stroke-width="1">
      <line x1="765" y1="698" x2="800" y2="664"/>
      <line x1="765" y1="790" x2="800" y2="824"/>
      <line x1="987" y1="664" x2="1021" y2="698"/>
      <line x1="987" y1="790" x2="1021" y2="824"/>
    </g>
  </svg>

  <section class="welcome">
    <h1 class="welcome-title">Welcome</h1>
    <p>Welcome to the exciting world of Kestrel College! Since opening our doors in 1985 we have evolved into one of Sydney’s largest, most successful training providers, welcoming thousands of young Australian and international students every year.</p>
    <p>Kestrel College offers a diverse range of government-approved courses, all designed to equip students with the skills required to succeed in today’s dynamic global workplace. Our courses also provide a pathway to university, with Diploma and Advanced Diploma graduates eligible for advanced standing at a range of popular Australian universities.</p>
    <p>As a Kestrel College student, you will be trained by leading industry professionals and enjoy access to some of the best training resources and learning technology available. Our commitment is to deliver practical, job-focused training in a fun and flexible learning environment.</p>
    <p>Whether your aim is to achieve employment success in your chosen field, continue to university or simply to learn while enjoying Sydney’s fantastic lifestyle, we look forward to welcoming you to Kestrel College and working with you to achieve your goals.</p>
  </section>

  <div class="photo photo-study" role="img" aria-label="Three students studying together at a laptop"></div>
  <div class="photo photo-group" role="img" aria-label="Group of smiling international students posing together"></div>
  <div class="photo photo-traveller" role="img" aria-label="Travel consultant holding a brochure in front of a world map"></div>

  <div class="brand-row">
    <div class="brand"><span class="brand-mark"></span><span class="brand-name">Kestrel English School</span></div>
    <div class="brand"><span class="brand-mark"></span><span class="brand-name">Kestrel College of Business &amp; Travel</span></div>
  </div>

</main>
</body>
</html>
```